New Theme For Our Sales Sheets and Full Brochure

I need a new theme for a refrigerated cooler display. This them will get used for approx. 10 different items as well as a Full Brochure. If the feedback is great, we will change our website to follow the same theme.

I want to see how you can create a clean, simple sales sheet that will highlight features and help customers picture their products in our displays.

I have included in the file uploads a sales sheet from the past that we want to create something totally different

Target Market(s)

Supermarkets

Industry/Entity Type

Sales

Font styles to use
Serif

Requirements
Must have
• A very attractive theme that helps a viewer picture THEIR products in the coolers.
• Only want to show (2) units on the sales sheet... (1) Curved Header and (1) Flat.
Nice to have
• Highlight the feature of either a Curved or Flat Header that is back lit.

```html
<!DOCTYPE html>
<html lang="en">
<head>
<meta charset="utf-8">
<title>Grab N Go Refrigerated Displays – Sales Sheet</title>
<link rel="stylesheet" href="https://fonts.googleapis.com/css2?family=Playfair+Display+SC:wght@400;700&family=Playfair+Display:wght@400;700&display=swap">
<style>
  :root {
    --red: #8e1b1f;
    --red-dark: #7a1519;
    --white: #ffffff;
    --ink: #1c1c1c;
    --backdrop: #dce6ec;
    --photo-warm: #9a6a3a;
    --photo-cool: #c9b48a;
  }
  * { box-sizing: border-box; margin: 0; padding: 0; }
  html, body { width: 1200px; height: 1200px; overflow: hidden; }
  body { background: var(--backdrop); font-family: "Playfair Display", serif; color: var(--ink); }

  .sheet {
    position: absolute; left: 170px; top: 40px;
    width: 860px; height: 1120px;
    background: var(--white);
    box-shadow: 0 20px 50px rgba(40,60,80,.18);
    overflow: hidden;
  }

  .brand {
    position: absolute; left: 0; right: 0; top: 48px;
    text-align: center;
    font-size: 30px; letter-spacing: 1px; color: var(--red);
  }

  .hero-photo {
    position: absolute; left: 0; top: 140px; width: 860px; height: 400px;
    background: linear-gradient(135deg, var(--photo-warm), var(--photo-cool) 45%, #b88a55 70%, var(--photo-warm));
  }

  .title-box {
    position: absolute; left: 385px; top: 345px; width: 475px; height: 130px;
    background: var(--red); color: var(--white);
    text-align: right; padding: 22px 30px 0 0;
  }
  .title-box h1 {
    font-family: "Playfair Display SC", serif; font-weight: 400;
    font-size: 58px; line-height: 1; letter-spacing: 2px;
  }
  .title-box p { font-size: 22px; font-weight: 700; margin-top: 4px; }

  .sizes {
    position: absolute; left: 40px; top: 580px; width: 290px; height: 36px;
    background: var(--red); color: var(--white);
    font-family: "Playfair Display SC", serif; font-size: 18px;
    padding: 6px 0 0 14px; white-space: nowrap;
  }

  .unit {
    position: absolute; left: 105px; width: 160px; height: 165px;
  }
  .unit--curved { top: 645px; background: linear-gradient(#2b3a78, #151515 55%); border-radius: 40px 40px 4px 4px; }
  .unit--flat { top: 835px; background: linear-gradient(#9b2226 0 20%, #9aa0a6 20% 70%, #b3252a 70%); border-radius: 6px; }

  .specs { position: absolute; left: 380px; top: 555px; right: 0; }
  .spec-head {
    background: var(--red); color: var(--white); height: 38px;
    font-family: "Playfair Display SC", serif; font-weight: 400; font-size: 24px;
    padding: 3px 0 0 12px;
  }
  .spec-list { list-style: none; padding: 12px 0 16px 14px; font-size: 20px; line-height: 1.6; font-weight: 700; }

  .footer {
    position: absolute; left: 0; right: 0; bottom: 0; height: 100px;
    background: var(--red-dark); color: var(--white);
  }
  .footer address {
    position: absolute; left: 250px; top: 14px; width: 300px;
    font-style: normal; text-align: center;
    font-family: "Playfair Display SC", serif; font-size: 16px; line-height: 1.5;
  }
  .contact { position: absolute; left: 610px; top: 16px; list-style: none; font-size: 11px; line-height: 2.1; }
  .contact li { display: flex; align-items: center; gap: 8px; text-transform: uppercase; letter-spacing: .5px; white-space: nowrap; }
  .contact svg { width: 15px; height: 15px; fill: none; stroke: var(--white); stroke-width: 1.6; }
</style>
</head>
<body>
  <article class="sheet">
    <div class="brand">Northfield Display Co.</div>

    <div class="hero-photo" role="img" aria-label="Row of glass-door refrigerated coolers stocked with packaged grab-and-go foods"></div>

    <div class="title-box">
      <h1>Grab N Go</h1>
      <p>Refrigerated Displays</p>
    </div>

    <div class="sizes">30", 36" &amp; 50" Sizes Available</div>

    <div class="unit unit--curved" role="img" aria-label="Countertop cooler with curved back-lit header"></div>
    <div class="unit unit--flat" role="img" aria-label="Countertop cooler with flat back-lit header"></div>

    <section class="specs">
      <h2 class="spec-head">Temperature Range</h2>
      <ul class="spec-list"><li>35-46 F</li></ul>
      <h2 class="spec-head">Power</h2>
      <ul class="spec-list"><li>115 Volt</li><li>9.8 Amp</li></ul>
      <h2 class="spec-head">Options</h2>
      <ul class="spec-list">
        <li>Custom Color</li>
        <li>Multiple Graphic Packages Available</li>
        <li>Curved or Flat Header Light Box</li>
      </ul>
    </section>

    <footer class="footer">
      <address>
        Northfield Display Co.<br>
        418 Lakeview Road<br>
        Maple Grove, IL 60190
      </address>
      <ul class="contact">
        <li><svg viewBox="0 0 16 16"><path d="M3 2l3 1 1 3-2 1a8 8 0 0 0 4 4l1-2 3 1 1 3-2 1C7 14 2 9 2 4z"/></svg>815-555-0142</li>
        <li><svg viewBox="0 0 16 16"><rect x="1.5" y="3.5" width="13" height="9"/><path d="M1.5 3.5l6.5 5 6.5-5"/></svg>sales@northfielddisplay.com</li>
        <li><svg viewBox="0 0 16 16"><path d="M2 8l6-5.5L14 8M4 6.5V14h8V6.5"/></svg>www.northfielddisplay.com</li>
      </ul>
    </footer>
  </article>
</body>
</html>
```